The Christian Teacher Life-Cycle

Look at the Lifecyle of the Christian School.
Look at the BLT logo.
I am looking for a Christian Teacher Lifecycle that represents the slides in the PP upload.
Our website is bramblewoodlearningtrust.org.
The design should include a summary design showing all four stages, and then four slides representing each of the stages as subsets of the summary design.
When a teacher is going through the Lifecycle, they are going on their Professional Learning Journey that takes 40 years to unfold.
All five should include a copyright 2026 BLT on them.

```html
<!DOCTYPE html>
<html lang="en">
<head>
<meta charset="utf-8">
<title>The Christian Teacher Life-Cycle – BLT</title>
<link href="https://fonts.googleapis.com/css2?family=Exo+2:wght@400;500;600;700;800&display=swap" rel="stylesheet">
<style>
  :root{
    --canvas:#4d4d4d;
    --blue:#1d72b8;
    --blue-light:#6aa6d8;
    --grey-block:#7b7b7b;
    --text:#595959;
    --bullet:#6d6d6d;
    --white:#ffffff;
  }
  *{margin:0;padding:0;box-sizing:border-box}
  html,body{width:1200px;height:1090px;overflow:hidden;background:var(--canvas);font-family:"Exo 2",sans-serif}
  .slide{position:absolute;width:515px;height:290px;background:var(--white);overflow:hidden}
  .footer{position:absolute;left:0;right:0;bottom:0;height:13px;background:var(--blue);color:var(--white);
    font-size:4.6px;font-weight:500;display:flex;justify-content:space-between;align-items:center;padding:0 19px 0 12px}
  .brand{position:absolute;left:14px;top:246px;font-size:19px;font-weight:600;color:var(--blue);letter-spacing:.5px}
  .title-bar{position:absolute;top:15px;left:50%;transform:translateX(-50%);display:flex;height:31px;
    font-weight:700;font-size:22px;color:var(--white);line-height:31px;white-space:nowrap;letter-spacing:.3px}
  .title-bar .main{background:var(--blue);padding:0 8px 0 9px}
  .title-bar .stage{background:var(--grey-block);padding:0 9px 0 6px}
  .body{position:absolute;top:62px;left:0;right:0;height:182px;display:flex;align-items:center}
  .school{width:var(--col);flex:none;margin-left:var(--off);text-align:center;display:flex;flex-direction:column;align-items:center}
  .tree{width:var(--tw);height:var(--th);border-radius:6px;
    background:radial-gradient(ellipse at 50% 45%,var(--blue) 0%,var(--blue-light) 60%,#e3eef8 100%);margin-bottom:6px}
  .school-name{color:var(--blue);font-weight:700;font-size:12.5px;line-height:1.18}
  .school-phase{color:var(--text);font-size:10px;margin-top:2px}
  .school-years{color:var(--text);font-size:10px;margin-top:2px}
  .divider{width:1.2px;align-self:stretch;background:var(--blue);margin:0 12px 0 8px;flex:none}
  .points{flex:1;padding-right:30px}
  .points h3{color:var(--blue);font-weight:700;font-size:14.5px;line-height:1.12;margin-bottom:6px}
  .points h3.large{font-size:21px;margin-bottom:8px}
  .points ul{list-style:none}
  .points li{position:relative;padding-left:13px;color:var(--text);font-size:11.3px;line-height:1.2;margin-bottom:5px}
  .points.compact li{font-size:11px;margin-bottom:4px}
  .points.dense li{font-size:11.1px;line-height:1.14;margin-bottom:3px}
  .points li::before{content:"";position:absolute;left:0;top:3.5px;width:6px;height:6px;background:var(--bullet)}
  .points li.cont{margin-top:-1px}
  .points li.cont::before{display:none}
  .points li span{display:block}
  /* overview slide */
  .overview-title{position:absolute;top:11px;left:97px;display:flex;height:22px;font-weight:700;font-size:16px;line-height:22px;color:var(--white)}
  .overview-title .main{background:var(--blue);padding:0 4px 0 5px}
  .overview-title .stage{background:var(--grey-block);padding:0 4px}
  .overview-lead{position:absolute;top:40px;left:100px;width:315px;text-align:center;color:var(--blue);font-size:7.6px;font-weight:500;line-height:1.38}
  .stage-tree{position:absolute;top:86px;width:60px;height:60px;border-radius:4px;
    background:radial-gradient(ellipse at 50% 45%,var(--blue) 0%,var(--blue-light) 60%,#e3eef8 100%)}
  .stage-label{position:absolute;top:149px;width:90px;text-align:center;line-height:1.15}
  .stage-label b{display:block;color:var(--blue);font-size:6.1px;font-weight:700}
  .stage-label small{display:block;color:var(--text);font-size:4.8px}
  .stage-box{position:absolute;top:189px;height:27px;background:var(--blue);border-radius:2px;color:var(--white);text-align:center;padding-top:3px}
  .stage-box b{display:block;font-size:6.2px;font-weight:700;text-decoration:underline;text-underline-offset:1px;margin-bottom:2px}
  .stage-box span{display:block;font-size:4.5px;line-height:1.2}
  .flow{position:absolute;left:0;top:0}
</style>
</head>
<body>

<!-- Overview -->
<section class="slide" style="left:62px;top:64px">
  <h1 class="overview-title"><span class="main">BLT CHRISTAIN SCHOOL</span><span class="stage">LIFECYCLE</span></h1>
  <p class="overview-lead">All are good. The only sin is not growing. It is a 40 year career-long Professional Learning Journey. I want to grow so that children and teenagers will become more than before. They are also on a life-long Personal Learning Journey.</p>

  <div class="stage-tree" role="img" aria-label="Seedling being watered" style="left:40px"></div>
  <div class="stage-tree" role="img" aria-label="Young leafy tree" style="left:159px"></div>
  <div class="stage-tree" role="img" aria-label="Full mature tree" style="left:279px"></div>
  <div class="stage-tree" role="img" aria-label="Old tree shedding leaves" style="left:407px"></div>

  <div class="stage-label" style="left:25px"><b>The Enthusiastic<br>Christian School</b><small>(ENTREPRENEURIAL)</small><small>0–10 years</small></div>
  <div class="stage-label" style="left:144px"><b>The Confident<br>Christian School</b><small>(ADOLESCENT)</small><small>10–15 years</small></div>
  <div class="stage-label" style="left:264px"><b>The Inspired<br>Christian School</b><small>(MATURE)</small><small>15–30+ years</small></div>
  <div class="stage-label" style="left:392px"><b>The Proud<br>Christian School</b><small>(DYING)</small><small>20+ years</small></div>

  <svg class="flow" width="515" height="290" aria-hidden="true">
    <defs><marker id="ah" markerWidth="6" markerHeight="6" refX="5" refY="3" orient="auto"><path d="M0,0 L6,3 L0,6 z" fill="#7b7b7b"/></marker></defs>
    <g fill="none" stroke="#7b7b7b" stroke-width="1.3" marker-end="url(#ah)">
      <path d="M108,142 Q140,122 150,138"/>
      <path d="M232,142 Q264,122 275,138"/>
      <path d="M351,142 Q383,122 398,138"/>
      <path d="M103,202 L136,202"/>
      <path d="M236,202 L262,202"/>
      <path d="M356,202 L382,202"/>
    </g>
  </svg>

  <div class="stage-box" style="left:47px;width:45px"><b>STAGE 1</b><span>The focus is<br>on “I”</span></div>
  <div class="stage-box" style="left:146px;width:85px"><b>STAGE 2</b><span>Becoming part of the Christian<br>Professional Learning Community</span></div>
  <div class="stage-box" style="left:266px;width:86px"><b>STAGE 3</b><span>Learning leadership within the<br>faculty culture / CPLC</span></div>
  <div class="stage-box" style="left:385px;width:105px"><b>STAGE 4</b><span>So good, I am “invisible”; I have let go of<br>control and share it with my children/teens</span></div>

  <div class="brand">BLT</div>
  <footer class="footer"><span>© 2026 Bramblewood Learning Trust - Leadership Pathway Cohort: Steward</span><span>Mission Delivery</span></footer>
</section>

<!-- Stage 1 -->
<section class="slide" style="left:629px;top:64px;--col:150px;--off:38px;--tw:134px;--th:72px">
  <h2 class="title-bar"><span class="main">LEARNING JOURNEY</span><span class="stage">STAGE 1</span></h2>
  <div class="body">
    <div class="school">
      <div class="tree" role="img" aria-label="Seedling being watered from a watering can"></div>
      <div class="school-name">The Enthusiastic<br>Christian School</div>
      <div class="school-phase">(ENTREPRENEURIAL)</div>
      <div class="school-years">0–10 years</div>
    </div>
    <div class="divider"></div>
    <div class="points compact">
      <h3 class="large">The focus is on “I”</h3>
      <ul>
        <li>Fundamental skills dominate such as classroom management</li>
        <li>Curriculum is where I spend my time</li>
        <li>I am a sponge rather than a contributor</li>
        <li>I see myself as a learner</li>
        <li>I reflect on my practice</li>
      </ul>
    </div>
  </div>
  <div class="brand">BLT</div>
  <footer class="footer"><span>© 2026 Bramblewood Learning Trust - Leadership Pathway Cohort: Steward</span><span>Mission Delivery</span></footer>
</section>

<!-- Stage 2 -->
<section class="slide" style="left:62px;top:408px;--col:130px;--off:40px;--tw:122px;--th:108px">
  <h2 class="title-bar"><span class="main">LEARNING JOURNEY</span><span class="stage">STAGE 2</span></h2>
  <div class="body">
    <div class="school">
      <div class="tree" role="img" aria-label="Young leafy tree on a grassy mound"></div>
      <div class="school-name">The Confident<br>Christian School</div>
      <div class="school-phase">(ADOLESCENT)</div>
      <div class="school-years">10-15 years</div>
    </div>
    <div class="divider"></div>
    <div class="points">
      <h3>Becoming part of the Christian Professional Learning Community</h3>
      <ul>
        <li>My Christian Professional Learning Community is important to me as a place where I give and take</li>
        <li>I recognize that “we” is more powerful for the child than “I”</li>
        <li>I know my curriculum - I am more focused on how, on pedagogy</li>
        <li><span>I assess relevant and effective assessment tools</span><span>I reflect on my practice</span></li>
      </ul>
    </div>
  </div>
  <div class="brand">BLT</div>
  <footer class="footer"><span>© 2026 Bramblewood Learning Trust - Leadership Pathway Cohort: Steward</span><span>Mission Delivery</span></footer>
</section>

<!-- Stage 3 A -->
<section class="slide" style="left:629px;top:408px;--col:130px;--off:37px;--tw:118px;--th:112px">
  <h2 class="title-bar"><span class="main">LEARNING JOURNEY</span><span class="stage">STAGE 3 (A)</span></h2>
  <div class="body">
    <div class="school">
      <div class="tree" role="img" aria-label="Full mature tree with wide canopy"></div>
      <div class="school-name">The Inspired<br>Christian School</div>
      <div class="school-phase">(MATURE)</div>
      <div class="school-years">15–30+ years</div>
    </div>
    <div class="divider"></div>
    <div class="points" style="padding-right:14px">
      <h3>Learning leadership within the faculty culture / CPLC</h3>
      <ul>
        <li><span>I lead in my Christian Professional Learning Community</span><span>Ensuring my colleagues continue to grow is critical to me</span></li>
        <li>Together, we are humble in understanding where we still need to go</li>
        <li><span>My colleagues see me as an important resource</span><span>I am a master of growth</span></li>
        <li>I help my colleagues reflect</li>
      </ul>
    </div>
  </div>
  <div class="brand">BLT</div>
  <footer class="footer"><span>© 2026 Bramblewood Learning Trust - Leadership Pathway Cohort: Steward</span><span>Mission Delivery</span></footer>
</section>

<!-- Stage 3 B -->
<section class="slide" style="left:62px;top:753px;--col:130px;--off:34px;--tw:118px;--th:112px">
  <h2 class="title-bar"><span class="main">LEARNING JOURNEY</span><span class="stage">STAGE 3 (B)</span></h2>
  <div class="body">
    <div class="school">
      <div class="tree" role="img" aria-label="Full mature tree with wide canopy"></div>
      <div class="school-name">The Inspired<br>Christian School</div>
      <div class="school-phase">(MATURE)</div>
      <div class="school-years">15–30+ years</div>
    </div>
    <div class="divider"></div>
    <div class="points">
      <h3>Learning leadership within the faculty culture / CPLC</h3>
      <ul>
        <li style="margin-bottom:4px">I move to position the child as the owner of their own learning</li>
        <li style="margin-bottom:4px">I give up control so the child can gain control</li>
        <li class="cont" style="margin-bottom:4px">The child becomes an architect in their curriculum</li>
        <li style="margin-bottom:4px">The child becomes a collaborator in the how</li>
        <li style="margin-bottom:4px">I am more a learner than a teacher</li>
        <li style="margin-bottom:4px">I am a master of pedagogies</li>
        <li style="margin-bottom:0">I reflect on my practice through the eyes of children</li>
      </ul>
    </div>
  </div>
  <div class="brand">BLT</div>
  <footer class="footer"><span>© 2026 Bramblewood Learning Trust - Leadership Pathway Cohort: Steward</span><span>Mission Delivery</span></footer>
</section>

<!-- Stage 4 -->
<section class="slide" style="left:629px;top:753px;--col:130px;--off:37px;--tw:116px;--th:112px">
  <h2 class="title-bar"><span class="main">LEARNING JOURNEY</span><span class="stage">STAGE 4</span></h2>
  <div class="body" style="top:56px;height:192px">
    <div class="school">
      <div class="tree" role="img" aria-label="Old tree with bare branches shedding leaves"></div>
      <div class="school-name">The Proud<br>Christian School</div>
      <div class="school-phase">(DYING)</div>
      <div class="school-years">20+ years</div>
    </div>
    <div class="divider"></div>
    <div class="points dense" style="padding-right:12px">
      <h3>So good, I am “invisible”; I have let go of control and share it with my children/teens</h3>
      <ul>
        <li>I am comfortable both in making the child owner and in taking on leadership roles with colleagues</li>
        <li>Children come to and stay at the school because I am there</li>
        <li>I want and work to ensure that every child to succeed</li>
        <li>I want and work to ensure that every one of my colleagues to succeed</li>
        <li>I am a master of severalpedagogies</li>
        <li>I am a master of metacognition</li>
        <li>I see myself as a learner</li>
        <li style="margin-bottom:0">I reflect on my practice with my children / teens</li>
      </ul>
    </div>
  </div>
  <div class="brand">BLT</div>
  <footer class="footer"><span>© 2026 Bramblewood Learning Trust - Leadership Pathway Cohort: Steward</span><span>Mission Delivery</span></footer>
</section>

</body>
</html>
```